Require stock illustrations for BrimQuay website

We need the 8 screenshots in the 'Features' section (also attached) to be individually recreated as illustrations using a style/colors similar to the image on the home page:

http://images.brimquay-example.com/AgentPictures/BrimQuayV2/template/index.html#_

The illustrations are meant to be abstract versions of the actual images

Font styles to use
Sans Serif

Requirements
Must have
• 1. 8 vector images including png outputs
2. style of images should match the style/colors of the image on the home page
3. all images should possess the same aspect ratio of 545 width x 344 height

```html
<!DOCTYPE html>
<html lang="en">
<head>
<meta charset="utf-8">
<title>BrimQuay Features Illustration</title>
<link rel="stylesheet" href="https://fonts.googleapis.com/css2?family=Open+Sans:wght@400;700&display=swap">
<style>
  :root {
    --canvas: #f4f5f2;
    --header: #232225;
    --header-bar: #ffffff;
    --title: #4d4d4f;
    --line: #a3a3a3;
    --orange: #ff6633;
    --green: #99d900;
    --yellow: #ffd466;
    --teal: #26c0c8;
    --icon: #ffffff;
  }
  * { margin: 0; padding: 0; box-sizing: border-box; }
  html, body {
    width: 1200px;
    height: 757px;
    overflow: hidden;
    background: var(--canvas);
    font-family: "Open Sans", sans-serif;
  }
  .canvas {
    position: relative;
    width: 1200px;
    height: 757px;
    background: var(--canvas);
  }
  .page-header {
    position: absolute;
    left: 48px;
    top: 18px;
    width: 1108px;
    height: 66px;
    background: var(--header);
  }
  .page-header__title {
    position: absolute;
    left: 25px;
    top: 17px;
    width: 361px;
    height: 29px;
    background: var(--header-bar);
  }
  .feature {
    position: absolute;
    left: 48px;
    width: 1108px;
    height: 139px;
  }
  .feature--view { top: 110px; }
  .feature--mail { top: 273px; }
  .feature--like { top: 438px; }
  .feature--share { top: 601px; }
  .feature__tile {
    position: absolute;
    left: 0;
    top: 0;
    width: 201px;
    height: 139px;
    display: flex;
    align-items: center;
    justify-content: center;
  }
  .feature--view .feature__tile { background: var(--orange); }
  .feature--mail .feature__tile { background: var(--green); }
  .feature--like .feature__tile { background: var(--yellow); }
  .feature--share .feature__tile { background: var(--teal); }
  .feature__tile svg { width: 92px; height: 92px; }
  .feature__heading {
    position: absolute;
    left: 267px;
    top: 7px;
    width: 279px;
    height: 22px;
    background: var(--title);
  }
  .feature__body {
    position: absolute;
    left: 271px;
    top: 42px;
    display: flex;
    flex-direction: column;
    gap: 11px;
  }
  .feature__line {
    height: 11px;
    background: var(--line);
  }
</style>
</head>
<body>
<main class="canvas">
  <header class="page-header"><div class="page-header__title"></div></header>

  <section class="feature feature--view">
    <div class="feature__tile">
      <svg viewBox="0 0 100 100" fill="none" stroke="var(--icon)" stroke-width="7">
        <path d="M8 50 Q50 12 92 50 Q50 88 8 50 Z"/>
        <circle cx="50" cy="50" r="15"/>
        <circle cx="50" cy="50" r="5" fill="var(--icon)" stroke="none"/>
      </svg>
    </div>
    <div class="feature__heading"></div>
    <div class="feature__body">
      <div class="feature__line" style="width:770px"></div>
      <div class="feature__line" style="width:715px"></div>
      <div class="feature__line" style="width:733px"></div>
      <div class="feature__line" style="width:634px"></div>
    </div>
  </section>

  <section class="feature feature--mail">
    <div class="feature__tile">
      <svg viewBox="0 0 100 100" fill="none" stroke="var(--icon)" stroke-width="5" stroke-linejoin="round">
        <rect x="8" y="22" width="84" height="56"/>
        <path d="M8 22 L50 56 L92 22"/>
        <path d="M8 78 L38 46 M92 78 L62 46"/>
      </svg>
    </div>
    <div class="feature__heading"></div>
    <div class="feature__body">
      <div class="feature__line" style="width:759px"></div>
      <div class="feature__line" style="width:768px"></div>
      <div class="feature__line" style="width:750px"></div>
      <div class="feature__line" style="width:334px"></div>
    </div>
  </section>

  <section class="feature feature--like">
    <div class="feature__tile">
      <svg viewBox="0 0 100 100">
        <path fill="var(--icon)" d="M50 86 L14 50 C2 38 6 16 26 14 C38 13 46 20 50 28 C54 20 62 13 74 14 C94 16 98 38 86 50 Z"/>
      </svg>
    </div>
    <div class="feature__heading"></div>
    <div class="feature__body">
      <div class="feature__line" style="width:715px"></div>
      <div class="feature__line" style="width:759px"></div>
      <div class="feature__line" style="width:733px"></div>
      <div class="feature__line" style="width:330px"></div>
    </div>
  </section>

  <section class="feature feature--share">
    <div class="feature__tile">
      <svg viewBox="0 0 100 100">
        <path d="M72 20 L28 50 L72 80" fill="none" stroke="var(--icon)" stroke-width="7"/>
        <circle cx="72" cy="20" r="13" fill="var(--icon)"/>
        <circle cx="28" cy="50" r="13" fill="var(--icon)"/>
        <circle cx="72" cy="80" r="13" fill="var(--icon)"/>
      </svg>
    </div>
    <div class="feature__heading"></div>
    <div class="feature__body">
      <div class="feature__line" style="width:788px"></div>
      <div class="feature__line" style="width:746px"></div>
      <div class="feature__line" style="width:770px"></div>
      <div class="feature__line" style="width:110px"></div>
    </div>
  </section>
</main>
</body>
</html>
```